LumaLearn.net the Free Online Tutorial Needs a New Web Design

We need a new web design for our existing website, LumaLearn.net. We provide a Free Online Tutorial of any code, like HTML, CSS, PHP, KQuery, javascript etc, including online editor.
We would like to see designs that interesting, simple, interactive, and be a very comfortable place to read in a long time.
We need 2 pages design for:
1. Home Page (http://lumalearn.net) and
2. Listing Page (http://lumalearn.net/tutorial/833/sql/sql-basics/sql-and-or-operator.html)
For Listing Page We need nice "Left Menu" at left side and Content Page (min 728px) at right side.
I need File PSD and/or Vector Only, without HTML code.

```html
<!DOCTYPE html>
<html lang="en">
<head>
<meta charset="utf-8">
<title>SQL AND / OR Operators – LumaLearn</title>
<link href="https://fonts.googleapis.com/css2?family=Roboto:wght@400;500;700&display=swap" rel="stylesheet">
<style>
:root{
  --ink:#333;
  --muted:#666;
  --header:#111;
  --nav:#1d6fd8;
  --nav-active:#f2453d;
  --page:#ececec;
  --white:#fff;
  --line:#d9d9d9;
  --blue:#2b78c9;
  --red:#e8413a;
  --green:#2f9d27;
  --btn:#72b51c;
  --th:#e4e4e4;
  --box:#e6e6e6;
  --footer:#2d2d2d;
  --footer-bottom:#1f1f1f;
  --footer-text:#8a8a8a;
}
*{box-sizing:border-box;margin:0;padding:0}
html,body{width:1200px;height:3093px;overflow:hidden}
body{background:var(--page);font-family:"Roboto",Arial,sans-serif;color:var(--ink);position:relative}
.site-header{position:absolute;top:0;left:0;width:1200px;height:128px;background:var(--header)}
.brand{position:absolute;left:90px;top:44px;display:flex;align-items:center;gap:12px;color:var(--white);font-size:38px;font-weight:700;letter-spacing:-.5px}
.brand-mark{width:38px;height:38px;background:var(--nav)}
.account-links{position:absolute;right:90px;top:55px;color:var(--white);font-size:14px}
.account-links span{margin:0 6px}
.main-nav{position:absolute;top:128px;left:0;width:1200px;height:66px;background:var(--nav)}
.main-nav a{position:absolute;top:0;line-height:66px;color:var(--white);font-size:14px;text-decoration:none}
.main-nav .active{background:var(--nav-active);width:88px;text-align:center;left:89px}
.search{position:absolute;left:893px;top:14px;width:218px;height:38px;background:var(--white);border-radius:3px;font-size:11px;color:#444;padding:12px 12px}
.search svg{position:absolute;right:10px;top:9px}
.container{position:absolute;left:89px;top:231px;width:1021px;height:2538px;background:var(--white);border:1px solid var(--line)}
.sidebar{position:absolute;left:0;top:0;width:241px;height:100%;border-right:1px solid var(--line);padding:34px 0 0 30px}
.sidebar h2{color:var(--red);font-size:17px;font-weight:400;line-height:28px}
.sidebar h3{color:var(--blue);font-size:15px;font-weight:400;line-height:24px;margin-top:18px}
.sidebar h2 + h3{margin-top:0}
.sidebar li{list-style:none;font-size:12px;line-height:21px;color:#444}
.content{position:absolute;left:268px;top:0;width:721px;height:100%}
.content > *{position:absolute;left:0;width:721px}
.promo{height:66px}
.promo-title{color:var(--blue);font-size:27px;letter-spacing:.5px}
.promo-sub{color:#444;font-size:14px;margin-top:6px}
.promo-btn{position:absolute;left:534px;top:4px;width:56px;height:52px;background:var(--nav);border-radius:3px}
.promo-btn svg{position:absolute;left:17px;top:13px}
.promo-dots{position:absolute;left:224px;top:66px;display:flex;gap:6px}
.promo-dots i{width:7px;height:7px;border-radius:50%;border:1px solid #555}
.promo-dots i:first-child{background:#333}
.promo-tag{position:absolute;left:697px;top:0;color:var(--blue);font-size:12px}
.page-title{font-size:24px;font-weight:400;color:#222;line-height:30px}
.pager{height:27px;border-bottom:2px solid var(--line);display:flex;justify-content:space-between;font-size:14px;color:var(--green);line-height:18px}
.lead{font-size:13px;line-height:20px;color:#444}
.section-title{font-size:19px;font-weight:400;color:#222;line-height:24px}
.note{font-size:13px;line-height:23px;color:#444;padding-left:6px}
.data{border-collapse:collapse;box-shadow:0 2px 4px rgba(0,0,0,.18);border:1px solid var(--line);font-size:12.5px;table-layout:fixed}
.data th{background:var(--th);font-weight:400;height:45px;text-align:left;padding-left:20px;border-right:1px solid #cfcfcf}
.data td{height:45px;padding-left:20px;border-top:1px solid var(--line);border-right:1px solid #eee}
.example{left:6px!important;width:713px!important;background:var(--box);border:1px solid #d6d6d6}
.example-title{position:absolute;left:18px;top:7px;font-size:17px;color:#333}
.code{position:absolute;left:18px;width:672px;background:var(--white);border-left:5px solid var(--btn);box-shadow:0 2px 4px rgba(0,0,0,.2);padding:14px 18px;font-size:13px;line-height:20px;color:#333}
.try{position:absolute;left:18px;width:108px;height:28px;background:var(--btn);color:var(--white);font-size:12px;line-height:28px;text-align:center;border-radius:2px}
.banner{left:6px!important;width:713px!important;height:89px;background:linear-gradient(90deg,#5a5a5a 0%,#8a2a22 30%,#c4221a 60%,#b81d16 100%)}
.site-footer{position:absolute;left:0;top:2788px;width:1200px;height:237px;background:var(--footer)}
.footer-col{position:absolute;top:38px;width:150px}
.footer-col h4{font-size:14px;font-weight:400;color:#ddd;margin-bottom:14px}
.footer-col li{list-style:none;font-size:11px;color:var(--footer-text);line-height:33px;border-bottom:1px solid #4a4a4a;height:34px}
.social li{border:none;display:flex;align-items:center;gap:14px;height:40px;line-height:40px}
.social i{width:34px;height:34px;border:1px solid #777;border-radius:50%}
.footer-bottom{position:absolute;left:0;top:3025px;width:1200px;height:68px;background:var(--footer-bottom);color:#888;font-size:11px;text-align:center;line-height:62px}
</style>
</head>
<body>
<header class="site-header">
  <div class="brand"><span class="brand-mark"></span>LumaLearn</div>
  <div class="account-links">Login<span>|</span>Sign Up<span>|</span>Forgot Password?</div>
</header>
<nav class="main-nav">
  <a class="active">HOME</a>
  <a style="left:200px">HTML</a>
  <a style="left:284px">CSS</a>
  <a style="left:354px">JAVASCRIPT</a>
  <a style="left:482px">PHP</a>
  <a style="left:556px">SQL</a>
  <a style="left:626px">KQUERY</a>
  <a style="left:726px">JSON</a>
  <a style="left:806px">MORE</a>
  <div class="search">Search by Seeker Engine
    <svg width="18" height="18" viewBox="0 0 18 18"><circle cx="7" cy="7" r="5.5" fill="none" stroke="#222" stroke-width="2.4"/><path d="M11 11l5.5 5.5" stroke="#222" stroke-width="2.6"/></svg>
  </div>
</nav>

<div class="container">
  <aside class="sidebar">
    <h2>SQL Tutorial</h2>
    <h3>SQL Introduction</h3>
    <ul><li>SQL Introduction</li><li>SQL Syntax</li><li>SQL Data Types (Ledgerly)</li><li>SQL Data Type (MiniBase)</li><li>SQL Data Types (Orbis)</li><li>SQL Data Types (DataHall)</li><li>SQL Reference</li><li>SQL Terminology</li></ul>
    <h3>SQL Basics</h3>
    <ul><li>SQL And / Or</li><li>SQL DELETE</li><li>SQL DISTINCT</li><li>SQL Group By</li><li>SQL Insert</li><li>SQL Not</li><li>SQL Order By</li><li>SQL Select</li><li>SQL Update</li><li>SQL Where</li><li>SQL Create Database</li><li>SQL Create Table</li><li>SQL Drop</li><li>SQL TRUNCATE</li></ul>
    <h3>SQL Advanced</h3>
    <ul><li>SQL Alias</li><li>SQL Alter</li><li>SQL Auto-increment</li><li>SQL Between</li><li>SQL Create Index</li><li>SQL In</li><li>SQL Isnull()</li><li>SQL Like</li><li>SQL Null Values</li><li>SQL Select Into</li><li>SQL Union</li><li>SQL Top</li><li>SQL View</li><li>SQL Wildcards</li></ul>
    <h3>SQL Constraints</h3>
    <ul><li>SQL Constraints Overview</li><li>SQL Check</li><li>SQL Default</li><li>SQL Not Null</li><li>SQL Primary Key</li><li>SQL Foreign Key</li><li>SQL Unique</li></ul>
    <h3>SQL Joins</h3>
    <ul><li>SQL Constraints Overview</li><li>SQL Check</li><li>SQL Default</li><li>SQL Not Null</li><li>SQL Primary Key</li><li>SQL Foreign Key</li><li>SQL Unique</li></ul>
    <h3>SQL Functions</h3>
    <ul><li>SQL Functions Overview</li><li>SQL AVG ()</li><li>SQL COUNT()</li><li>SQL FIRST()</li><li>SQL FORMAT()</li><li>SQL LAST()</li><li>SQL LCASE() / LOWER()</li><li>SQL LEN()</li><li>SQL MAX()</li><li>SQL MID()</li><li>SQL MIN()</li><li>SQL NOW()</li><li>SQL ROUND()</li><li>SQL SUM()</li><li>SQL UCASE() / UPPER()</li></ul>
  </aside>

  <main class="content">
    <div class="promo" style="top:33px">
      <div class="promo-title">FREE CLOUD SERVER</div>
      <div class="promo-sub">Give Us a Try and We'll Give You a Month, On the House. Chat for Info!</div>
      <div class="promo-btn"><svg width="22" height="26" viewBox="0 0 22 26"><path d="M4 2l13 11L4 24" fill="none" stroke="#fff" stroke-width="3"/></svg></div>
      <div class="promo-dots"><i></i><i></i></div>
      <div class="promo-tag">▷</div>
    </div>

    <h1 class="page-title" style="top:156px">SQL AND / OR Operators</h1>
    <div class="pager" style="top:197px"><span>« Previous</span><span>Next Chapter »</span></div>

    <p class="lead" style="top:239px">The AND &amp; OR operators are used to filter records based on more than one condition.</p>
    <p class="lead" style="top:272px">The AND operator displays a record if <b>both</b> the first condition and the second condition is true.</p>
    <p class="lead" style="top:305px">The OR operator displays a record if <b>either</b> the first condition or the second condition is true.</p>

    <h2 class="section-title" style="top:355px">Example with AND Operator</h2>
    <p class="lead" style="top:380px">Consider the following "Buyers" table:</p>

    <table class="data" style="top:425px">
      <colgroup><col style="width:103px"><col style="width:142px"><col style="width:155px"><col style="width:95px"><col style="width:118px"><col style="width:108px"></colgroup>
      <tr><th>BuyerID</th><th>BuyerName</th><th>BuyerAddress</th><th>City</th><th>Country</th><th>Deposit</th></tr>
      <tr><td>1</td><td>David Clinton</td><td>Blue Lake 123</td><td>New York</td><td>USA</td><td>435.45</td></tr>
      <tr><td>2</td><td>Shea Roxanne</td><td>Santa Rose 123</td><td>Liverpool</td><td>England</td><td>234.12</td></tr>
      <tr><td>3</td><td>Bryan de Lima</td><td>Corcovado Street</td><td>Rio de Janeir</td><td>Brazil</td><td>534.22</td></tr>
      <tr><td>4</td><td>Tjen Chun Yen</td><td>Zhonghua Street 456</td><td>Shanghai</td><td>China</td><td>234.12</td></tr>
      <tr><td>5</td><td>Sheila White</td><td>Santa San Marine 456</td><td>New York</td><td>USA</td><td>234.12</td></tr>
      <tr><td>6</td><td>Bryan Clinton</td><td>Blue Lake 123</td><td>Sidney</td><td>Australia</td><td>534.22</td></tr>
      <tr><td>7</td><td>David Clinton</td><td>Blue Lake 123</td><td>Sidney</td><td>Australia</td><td>4361.87</td></tr>
      <tr><td>8</td><td>Tjen Chun Yen</td><td>Blue Lake 123</td><td>Singapore</td><td>Singapore</td><td>308.33</td></tr>
      <tr><td>9</td><td>Sheila White</td><td>Santa San Marine 456</td><td>Sidney</td><td>Australia</td><td>435.45</td></tr>
    </table>

    <p class="note" style="top:895px">In this example, select only the "Buyers" with the BuyerName equal to "David Clinton" AND the Country equal to<br>"Australia":</p>

    <div class="example" style="top:975px;height:196px">
      <div class="example-title">Example</div>
      <div class="code" style="top:37px">SELECT * FROM Buyers<br>WHERE BuyerName='David Clinton'<br>AND Country='Australia'</div>
      <div class="try" style="top:149px">Try it now &gt;&gt;</div>
    </div>

    <p class="note" style="top:1200px">The Following is the result of the above example:</p>
    <table class="data" style="top:1237px;left:6px;width:715px">
      <colgroup><col style="width:103px"><col style="width:142px"><col style="width:155px"><col style="width:95px"><col style="width:118px"><col style="width:102px"></colgroup>
      <tr><th>BuyerID</th><th>BuyerName</th><th>BuyerAddress</th><th>City</th><th>Country</th><th>Deposit</th></tr>
      <tr><td>1</td><td>David Clinton</td><td>Blue Lake 123</td><td>New York</td><td>USA</td><td>435.45</td></tr>
    </table>

    <h2 class="section-title" style="top:1376px;left:6px">Example with OR Operator</h2>
    <p class="note" style="top:1406px">In this example, select only the Buyers with the BuyerName equal to "Tjen Chun Yen" OR the BuyerName equal to<br>"Sheila White":</p>

    <div class="example" style="top:1464px;height:140px">
      <div class="code" style="top:14px">SELECT * FROM Buyers<br>WHERE BuyerName='Tjen Chun Yen' OR BuyerName='Sheila White'</div>
      <div class="try" style="top:99px">Try it now &gt;&gt;</div>
    </div>

    <p class="lead" style="top:1631px">The Following is the result of the above example:</p>
    <table class="data" style="top:1666px">
      <colgroup><col style="width:103px"><col style="width:142px"><col style="width:155px"><col style="width:95px"><col style="width:118px"><col style="width:108px"></colgroup>
      <tr><th>BuyerID</th><th>BuyerName</th><th>BuyerAddress</th><th>City</th><th>Country</th><th>Deposit</th></tr>
      <tr><td>1</td><td>David Clinton</td><td>Blue Lake 123</td><td>New York</td><td>USA</td><td>435.45</td></tr>
      <tr><td>2</td><td>Shea Roxanne</td><td>Santa Rose 123</td><td>Liverpool</td><td>England</td><td>234.12</td></tr>
      <tr><td>3</td><td>Bryan de Lima</td><td>Corcovado Street</td><td>Rio de Janeir</td><td>Brazil</td><td>534.22</td></tr>
      <tr><td>4</td><td>Tjen Chun Yen</td><td>Zhonghua Street 456</td><td>Shanghai</td><td>China</td><td>234.12</td></tr>
    </table>

    <div class="banner" style="top:1907px" role="img" aria-label="Advertisement banner for an emergency preparedness kit"></div>

    <h2 class="section-title" style="top:2025px;left:6px">Example with AND &amp; OR Operator</h2>
    <p class="note" style="top:2053px">In this example, select only the Buyers with the Country equal to "China" OR the Country equal to "Singapore" and<br>BuyerName equal to "Tjen Chun Yen":</p>

    <div class="example" style="top:2120px;height:138px">
      <div class="code" style="top:12px">SELECT * FROM Buyers<br>WHERE (Country='China' OR Country='Singapore') AND BuyerName ='Tjen Chun Yen'</div>
      <div class="try" style="top:94px">Try it now &gt;&gt;</div>
    </div>

    <p class="lead" style="top:2279px">The Following is the result of the above example:</p>
    <table class="data" style="top:2316px">
      <colgroup><col style="width:103px"><col style="width:142px"><col style="width:155px"><col style="width:95px"><col style="width:118px"><col style="width:108px"></colgroup>
      <tr><th>BuyerID</th><th>BuyerName</th><th>BuyerAddress</th><th>City</th><th>Country</th><th>Deposit</th></tr>
      <tr><td>1</td><td>David Clinton</td><td>Blue Lake 123</td><td>New York</td><td>USA</td><td>435.45</td></tr>
      <tr><td>2</td><td>Shea Roxanne</td><td>Santa Rose 123</td><td>Liverpool</td><td>England</td><td>234.12</td></tr>
    </table>

    <div class="pager" style="top:2470px;border-bottom:none;border-top:2px solid var(--line);padding-top:12px;height:34px"><span>« Previous</span><span>Next Chapter »</span></div>
  </main>
</div>

<footer class="site-footer">
  <div class="footer-col" style="left:97px"><h4>Random HTML5</h4><ul><li>img html5</li><li>Base Tag</li><li>tfoot tag in html</li><li>summary tag in html5</li></ul></div>
  <div class="footer-col" style="left:309px"><h4>Random Canvas</h4><ul><li>Canvas Image Loader</li><li>html5-canvas-rounded-corn...</li><li>Canvas Arc</li><li>Canvas Image Crop</li></ul></div>
  <div class="footer-col" style="left:524px"><h4>Random Javascript</h4><ul><li>JS String-HTML italics()</li><li>JS DOM Textarea</li><li>Javascript Browser Histor...</li><li>JS DOM TableRow</li></ul></div>
  <div class="footer-col" style="left:742px"><h4>Random Try it</h4><ul><li>aside tag example</li><li>br tag example</li><li>tt tag example</li><li>pre tag example</li></ul></div>
  <div class="footer-col social" style="left:965px"><h4>Follow us on :</h4><ul><li><i></i>Socialbook</li><li><i></i>Chirper</li><li><i></i>Pictogram</li></ul></div>
</footer>
<div class="footer-bottom">Copyright © 2014.. All Rights Reserved</div>
</body>
</html>
```